TALBRIDGE ELEVATOR CORP

LOOKING FOR BLACK MATTE BACKGROUND WITH GLOSS DESIGN
NEED RAISED UV ON LOGO AND LETTERING , WITH ROUNDED CORNERS AND COLORED EDGES ( FLOURECENT BLUE)

```html
<!DOCTYPE html>
<html lang="en">
<head>
<meta charset="utf-8">
<title>Talbridge Elevator Corp – Business Card</title>
<link rel="stylesheet" href="https://fonts.googleapis.com/css2?family=Exo+2:wght@400;600;800&display=swap">
<style>
  :root {
    --page: #ffffff;
    --card: #141414;
    --edge: #2f7ec4;
    --accent-green: #4fae45;
    --name-blue: #2f7ec4;
    --text: #f2f2f2;
    --logo-text: #d6d6d6;
    --emblem: #2f7ec4;
  }
  html, body {
    margin: 0;
    width: 1200px;
    height: 706px;
    overflow: hidden;
    background: var(--page);
    font-family: "Exo 2", sans-serif;
  }
  .canvas { position: relative; width: 1200px; height: 706px; }
  .card {
    position: absolute;
    top: 220px;
    width: 470px;
    height: 266px;
    background: var(--card);
    border: 2px solid var(--edge);
    border-radius: 20px;
    box-shadow: 6px 6px 7px rgba(0, 0, 0, 0.35);
    overflow: hidden;
  }
  .card--front { left: 91px; }
  .card--back { left: 635px; }

  .wordmark {
    position: absolute;
    margin: 0;
    text-align: center;
    color: var(--logo-text);
    font-weight: 800;
    text-transform: uppercase;
    line-height: 1;
  }
  .wordmark span { display: block; }
  .card--front .wordmark {
    left: 0; right: 0; top: 30px;
    font-size: 30px;
  }
  .card--front .wordmark span + span { margin-top: 3px; }

  .divider {
    position: absolute;
    left: 22px; right: 21px; top: 154px;
    height: 1px;
    background: var(--accent-green);
  }
  .name-flag {
    position: absolute;
    left: 0; top: 178px;
    width: 4px; height: 33px;
    background: var(--accent-green);
  }
  .person { position: absolute; left: 22px; top: 174px; }
  .person__name {
    margin: 0;
    color: var(--name-blue);
    font-weight: 600;
    font-size: 22px;
    line-height: 1;
    letter-spacing: 0.3px;
  }
  .person__role {
    margin: 3px 0 0;
    color: var(--text);
    font-size: 12.5px;
    font-weight: 400;
  }
  .address {
    position: absolute;
    right: 21px; top: 175px;
    margin: 0;
    color: var(--text);
    font-size: 12.5px;
    font-style: normal;
  }
  .contacts {
    position: absolute;
    right: 21px; top: 198px;
    margin: 0; padding: 0;
    list-style: none;
    color: var(--text);
    font-size: 12.5px;
  }
  .contacts li {
    display: flex;
    align-items: center;
    justify-content: flex-end;
    height: 16px;
    gap: 6px;
  }
  .contacts svg { width: 13px; height: 13px; flex: none; }

  .established {
    position: absolute;
    left: 240px; width: 200px; top: 112px;
    margin: 0;
    text-align: center;
    color: var(--text);
    font-size: 13px;
    letter-spacing: 0.3px;
  }
  .card--back .wordmark {
    left: 240px; width: 200px; top: 134px;
    font-size: 31px;
  }
  .card--back .wordmark span + span { margin-top: 6px; }
  .emblem {
    position: absolute;
    left: 57px; top: 104px;
    width: 140px; height: 140px;
    border-radius: 50%;
    background: var(--emblem);
  }
</style>
</head>
<body>
<main class="canvas">
  <section class="card card--front" aria-label="Card front">
    <h1 class="wordmark"><span>Talbridge</span><span>Elevator</span><span>Corp</span></h1>
    <div class="divider"></div>
    <div class="name-flag"></div>
    <div class="person">
      <p class="person__name">DANIEL HARTWELL</p>
      <p class="person__role">President</p>
    </div>
    <address class="address">2215 Harlow Ave, Bronx 10461</address>
    <ul class="contacts">
      <li>(718) 555-0147
        <svg viewBox="0 0 16 16" aria-hidden="true"><circle cx="8" cy="8" r="7" fill="none" stroke="#2f7ec4" stroke-width="1.3"/><path d="M5.3 4.6l1.4-.3.8 1.8-.9.7a5 5 0 0 0 2.6 2.6l.7-.9 1.8.8-.3 1.4c-3.5.2-6.3-2.6-6.1-6.1z" fill="#2f7ec4"/></svg>
      </li>
      <li>talbridgeelev@mailbox.com
        <svg viewBox="0 0 16 16" aria-hidden="true"><rect x="1.5" y="3.5" width="13" height="9" fill="none" stroke="#2f7ec4" stroke-width="1.3"/><path d="M1.5 3.5L8 9l6.5-5.5M1.5 12.5L6 8M14.5 12.5L10 8" fill="none" stroke="#2f7ec4" stroke-width="1.1"/></svg>
      </li>
      <li>www.talbridgeelevatorny.com
        <svg viewBox="0 0 16 16" aria-hidden="true"><circle cx="8" cy="8" r="7" fill="#2f7ec4"/><path d="M1 8h14M8 1v14M2.5 4.5h11M2.5 11.5h11" stroke="#141414" stroke-width="0.9"/><ellipse cx="8" cy="8" rx="3.2" ry="7" fill="none" stroke="#141414" stroke-width="0.9"/></svg>
      </li>
    </ul>
  </section>

  <section class="card card--back" aria-label="Card back">
    <div class="emblem"></div>
    <p class="established">ESTABLISHED 1978</p>
    <h2 class="wordmark"><span>Talbridge</span><span>Elevator</span><span>Corp</span></h2>
  </section>
</main>
</body>
</html>
```